Simple design for eCommerce retailer of Custom Cut Mirror Frames

We need a fresh design for our eCommerce store. Currently, we need a design for each page on the existing site.

Here is the site as it stands right now: glassvela.com

Here is a competitor site that we like. The owner really likes the block look for the home page: framorly.com

Here is a video we would like to feature: https://videohost.example/v/Kp7rTq2LmXa

Here is the color palate, emphasis on the green and purple: https://palettes.example/quiet-bay-theme-48271953/?showPublished=true

Here is an example of a landing page we are currently using: https://glassvela.com/lander-10-off-install/

Font for the site should be the google font Lato

Home page should include the following sections/blocks:

How it works
Shop now
Testimonials
Featured Products
Before and After Gallery
Updates

My team has been slow getting back to me with feedback. I'm pushing them to speed their process up.

Target Market(s)

Women, Ages 35-65+

Number of Pages Required

5+ page

Font styles to use
Sans Serif

Requirements
Must have
• -Before and after gallery
• -Star ratings
• -eCommerce look and feel
• -Info about being able to order free samples
• -Language from the checkmarks on the landing page
• -sleek product page
• -home page should be have a very modern design feel
Should not have
• Product Prices...the user has to use the calculator to determine the price of their purchase.
• Sliders

```html
<!DOCTYPE html>
<html lang="en">
<head>
<meta charset="utf-8">
<title>Glassvela – Custom Mirror Frame Kits</title>
<link href="https://fonts.googleapis.com/css2?family=Lato:wght@300;400;700;900&display=swap" rel="stylesheet">
<style>
:root{
  --teal:#5e9c99;
  --teal-dark:#44807d;
  --teal-deep:#2f5f5d;
  --purple:#a27bab;
  --purple-light:#b48cbc;
  --purple-footer:#9a78a3;
  --ink:#222326;
  --text:#4a4a4a;
  --muted:#8a8a8a;
  --soft:#f2f2f2;
  --white:#ffffff;
  --gold:#e4b43b;
}
*{box-sizing:border-box;margin:0;padding:0}
html,body{width:1200px;height:4592px;overflow:hidden}
body{font-family:'Lato',sans-serif;color:var(--text);background:var(--white);position:relative}
.abs{position:absolute}
a{color:inherit;text-decoration:none}
.btn{display:inline-block;font-weight:700;font-size:14px;letter-spacing:.5px;padding:14px 30px;text-transform:uppercase}
.btn-dark{background:var(--ink);color:var(--white);text-transform:none;font-size:15px}
.btn-outline{border:1px solid #bbb;color:var(--ink);background:var(--white);font-size:13px;padding:13px 24px}
.stars{color:var(--gold);letter-spacing:3px;font-size:14px}
.section-title{font-weight:300;font-size:30px;letter-spacing:1px;text-transform:uppercase;text-align:center}

/* top bar */
.topbar{top:0;left:0;width:1200px;height:30px;background:var(--teal-deep);color:#dfe9e8;font-size:12px}
.topbar .promo{left:110px;top:8px}
.topbar .account{right:110px;top:8px;display:flex;gap:24px}

/* header */
.header{top:30px;left:0;width:1200px;height:160px;background:var(--white)}
.brand{left:112px;top:60px;display:flex;align-items:center;gap:12px}
.brand .mark{width:34px;height:34px;border-radius:50%;background:var(--purple)}
.brand .name{font-size:34px;font-weight:700;color:var(--ink);letter-spacing:.5px}
.sample-banner{left:445px;top:42px;width:640px;height:82px;background:var(--ink);color:var(--white)}
.sample-banner .head{left:30px;top:14px;font-size:28px;font-weight:700}
.sample-banner .head em{font-style:normal;color:var(--purple-light)}
.sample-banner .sub{left:30px;top:52px;font-size:14px;color:#ccc}
.sample-banner .code{right:22px;top:23px;border:1px solid #bbb;padding:10px 16px;font-size:13px;font-weight:700;letter-spacing:.5px}

/* nav */
.nav{top:190px;left:0;width:1200px;height:48px;background:var(--teal)}
.nav ul{list-style:none;display:flex;position:absolute;left:150px;top:15px;color:var(--white);font-size:15px}
.nav li{margin-right:64px}
.nav li.active{border-bottom:2px solid var(--white);padding-bottom:4px}

/* hero */
.hero{top:238px;left:0;width:1200px;height:325px;overflow:hidden}
.hero-before{left:0;top:0;width:578px;height:325px;background:linear-gradient(135deg,#c9b29a 0%,#e5d6c2 45%,#a68d74 100%)}
.hero-after{left:578px;top:0;width:622px;height:325px;background:linear-gradient(135deg,#b49577 0%,#e2d2bd 45%,#8a6b4f 100%)}
.hero-shade{left:0;top:0;width:1200px;height:325px;background:rgba(0,0,0,.12)}
.hero h1{position:absolute;left:0;width:1200px;top:90px;text-align:center;color:var(--white);font-size:38px;font-weight:400;text-shadow:0 2px 6px rgba(0,0,0,.5)}
.hero h2{position:absolute;left:0;width:1200px;top:140px;text-align:center;color:var(--white);font-size:28px;font-weight:900;text-shadow:0 2px 6px rgba(0,0,0,.5)}
.hero .btn{position:absolute;left:522px;top:210px}
.hero .label{top:297px;width:578px;height:28px;background:rgba(96,156,153,.85);color:var(--white);font-size:14px;text-align:center;padding-top:6px}

/* intro */
.intro-kicker{top:597px;left:0;width:1200px;text-align:center;font-size:18px}
.intro-title{top:628px;left:0;width:1200px;text-align:center;font-size:32px;font-weight:400;letter-spacing:1px;color:var(--purple-light)}
.video{left:205px;top:793px;width:790px;height:391px;background:linear-gradient(120deg,#6d7b86 0%,#c7ccd0 40%,#e8e6e1 60%,#8f9aa3 100%)}
.video .play{left:363px;top:158px;width:66px;height:66px}
.video .controls{left:0;bottom:0;width:790px;height:36px;background:rgba(0,0,0,.75)}
.video .progress{left:60px;top:0;width:730px;height:3px;background:#666}
.intro-copy{top:1218px;left:110px;width:980px;font-size:13.5px;line-height:25px;text-align:center}
.checks{top:1423px;left:110px;width:980px;display:grid;grid-template-columns:repeat(3,1fr);row-gap:22px;column-gap:20px;font-size:13.5px}
.checks div{display:flex;align-items:center;gap:8px}
.checks svg{flex:none}
.intro-buttons{top:1588px;left:0;width:1200px;display:flex;justify-content:center;gap:18px}

/* how it works */
.how{top:1683px;left:0;width:1200px;height:459px;background:var(--soft)}
.how .section-title{position:absolute;top:56px;left:0;width:1200px;color:var(--ink)}
.step-card{top:141px;width:305px;height:304px;background:var(--white)}
.step-card .badge{position:absolute;left:118px;top:-20px;width:68px;height:68px;border-radius:50%;background:var(--purple-light);color:var(--white);text-align:center;font-size:11px;letter-spacing:1px;padding-top:14px;line-height:1.1}
.step-card .badge b{display:block;font-size:24px;font-weight:400}
.step-card .pic{position:absolute;left:28px;top:60px;width:250px;height:180px}
.step-card .cap{position:absolute;left:0;width:305px;top:262px;text-align:center;font-weight:700;font-size:14px;color:var(--teal-deep);letter-spacing:.5px}

/* featured */
.featured-title{top:2220px;left:0;width:1200px;color:var(--purple-light)}
.tile{width:290px;height:214px;overflow:hidden}
.tile .pic{position:absolute;left:0;top:0;width:290px;height:214px}
.tile .strip{position:absolute;left:0;top:130px;width:290px;height:52px;background:rgba(20,20,20,.55);text-align:center;color:var(--white);font-size:14px;padding-top:8px;letter-spacing:.5px}
.tile .strip .stars{display:block;font-size:12px;margin-top:2px}
.tile .shop{position:absolute;left:106px;top:188px;background:var(--purple-light);color:var(--white);font-size:11px;font-weight:700;padding:4px 12px;letter-spacing:.5px}
.tile.hover{border-top:4px solid var(--purple-light)}
.arrow-side{top:2500px;color:#aaa;font-size:46px;font-weight:300}
.featured-btn{top:2809px;left:535px}

/* before/after */
.ba{top:2922px;left:0;width:1200px;height:566px;background:linear-gradient(180deg,var(--teal) 0%,#6fa9a6 100%)}
.ba .section-title{position:absolute;left:113px;top:60px;text-align:left;color:var(--white);font-size:28px}
.ba-collage{left:113px;top:123px;width:467px;height:336px;background:var(--white);padding:8px;display:grid;grid-template-columns:1fr 1fr;gap:8px}
.ba-collage div{background:linear-gradient(135deg,#b79e86,#e6dccf 55%,#8f7560)}
.ba-text{left:612px;top:134px;width:480px;color:var(--white);font-size:15px;line-height:26px}
.ba-btn{left:700px;top:368px;border:1px solid rgba(255,255,255,.8);color:var(--white);font-size:13px;padding:12px 22px}
.ba-corner{width:40px;height:40px}

/* guarantee */
.guarantee{top:3488px;left:0;width:1200px;height:352px;background:#f7f7f7}
.guarantee .pic{position:absolute;top:0;height:352px}
.ribbon{left:658px;top:56px;width:420px;height:44px;background:var(--teal);color:var(--white);font-weight:700;font-size:19px;text-align:center;padding-top:11px;letter-spacing:.5px}
.ribbon-tail{top:64px;width:0;height:0;border-top:18px solid var(--teal-dark);border-bottom:18px solid var(--teal-dark)}
.guarantee .copy{left:600px;width:540px;top:136px;text-align:center;font-size:18px;line-height:30px}
.guarantee .btn{left:754px;top:240px}

/* testimonials */
.testi{top:3840px;left:0;width:1200px;height:352px;background:linear-gradient(135deg,#2b2a28 0%,#4a4540 50%,#2e2c2a 100%)}
.testi .section-title{position:absolute;top:55px;left:0;width:1200px;color:#cfcfcf}
.testi .quote{position:absolute;left:200px;top:128px;width:800px;color:#e6e6e6;font-size:16px;line-height:26px}
.testi .quote::before{content:"\201C";position:absolute;left:-30px;top:-14px;font-size:50px;color:#bbb}
.testi .who{position:absolute;left:0;width:1200px;top:220px;text-align:center;color:#bbb;font-size:12px}
.testi .stars{position:absolute;left:0;width:1200px;top:240px;text-align:center}
.testi .arr{position:absolute;top:150px;color:#888;font-size:40px;font-weight:300}

/* footer */
.footer{top:4192px;left:0;width:1200px;height:400px;background:var(--purple-footer);color:var(--white)}
.footer .brand{left:125px;top:50px}
.footer .brand .name{color:var(--white);font-size:28px}
.footer .brand .mark{background:var(--white);width:28px;height:28px}
.footer .contact{left:118px;top:132px;font-size:12px;line-height:22px}
.footer h4{font-size:13px;font-weight:700;letter-spacing:.5px;margin-bottom:14px}
.footer ul{list-style:none;font-size:12px;line-height:22px}
.footer .col{top:48px}
.footer .badge-shape{top:290px;width:56px;height:62px;background:var(--white)}
.footer .copy{left:118px;top:362px;font-size:11px;color:#f0e8f2}
</style>
</head>
<body>

<div class="abs topbar">
  <span class="abs promo">In San Diego, or South Orange County? Free In-Home Consultation &nbsp;&nbsp;(555) 014-2290</span>
  <span class="abs account"><span>My account</span><span>Cart (0)</span></span>
</div>

<header class="abs header">
  <div class="abs brand"><span class="mark"></span><span class="name">Glassvela</span></div>
  <div class="abs sample-banner">
    <span class="abs head">Get up to <em>7 Samples</em> FREE!</span>
    <span class="abs sub">Use code: freesample at checkout.</span>
    <span class="abs code">GET A FREE SAMPLE CODE</span>
  </div>
</header>

<nav class="abs nav">
  <ul>
    <li class="active">Home</li>
    <li>Shop Mirror Frames</li>
    <li>Custom Framed Mirrors</li>
    <li>How It Works</li>
    <li>Before &amp; After Gallery</li>
  </ul>
</nav>

<section class="abs hero">
  <div class="abs hero-before" role="img" aria-label="Bathroom vanity with an unframed wall mirror"></div>
  <div class="abs hero-after" role="img" aria-label="Same bathroom vanity with a bronze framed mirror"></div>
  <div class="abs hero-shade"></div>
  <h1>NO GIMMICKS, JUST GREAT FRAMES!</h1>
  <h2>100% SATISFACTION GUARANTEE!</h2>
  <a class="btn btn-dark">Shop Now</a>
  <div class="abs label" style="left:0">Before</div>
  <div class="abs label" style="left:578px;width:622px">After</div>
</section>

<p class="abs intro-kicker">Quick, Easy, and Affordable</p>
<h2 class="abs intro-title">CUSTOM MIRROR FRAME KITS</h2>

<div class="abs video" role="img" aria-label="Video still of a woman installing a mirror frame kit">
  <svg class="abs play" viewBox="0 0 66 66"><circle cx="33" cy="33" r="33" fill="rgba(20,20,20,.85)"/><path d="M26 20 L47 33 L26 46 Z" fill="#fff"/></svg>
  <div class="abs controls">
    <div class="abs progress"></div>
    <svg class="abs" style="left:14px;top:11px" width="120" height="16" viewBox="0 0 120 16"><path d="M2 2 L12 8 L2 14Z" fill="#fff"/><rect x="22" y="3" width="2" height="10" fill="#fff"/><path d="M26 3 L34 8 L26 13Z" fill="#fff"/><path d="M44 6 h4 l4 -4 v12 l-4 -4 h-4z" fill="#fff"/><text x="62" y="12" fill="#fff" font-size="10" font-family="Lato,sans-serif">0:00 / 2:24</text></svg>
    <svg class="abs" style="right:14px;top:11px" width="90" height="16" viewBox="0 0 90 16"><rect x="2" y="3" width="14" height="10" fill="none" stroke="#fff"/><circle cx="34" cy="8" r="5" fill="none" stroke="#fff" stroke-width="2"/><rect x="52" y="3" width="14" height="10" fill="none" stroke="#fff"/><path d="M74 3h5M74 3v4M88 13h-5M88 13v-4" stroke="#fff" stroke-width="2"/></svg>
  </div>
</div>

<p class="abs intro-copy">With residential construction costs rising, contractors and homeowners often choose to install sheet glass mirrors in bathrooms and living spaces. While this is functional and economical, these mirrors often lack a unique style and decor enhancement of a hanging custom mirror frame. Instead, get Custom Framed Mirrors built to your specifications. Simply choose your style and enter your size. We have many mirror frame kits to fit your needs. Whether you are looking for one mirror frame or several mirror frames, we can make your mirrors look custom and revitalized. So whether you are looking to refresh your bathroom mirror or any mirror in your house – Our custom mirror frame kit is easy to install too. So be like the fairy-tale queen and say "mirror mirror" and you too can breathe new life into your bathroom mirror.</p>

<div class="abs checks">
  <div><svg width="16" height="16" viewBox="0 0 16 16"><rect x="1" y="3" width="12" height="12" fill="none" stroke="#a27bab"/><path d="M4 8 l3 3 l8 -9" fill="none" stroke="#a27bab" stroke-width="2"/></svg>DIY mirror framing kit</div>
  <div><svg width="16" height="16" viewBox="0 0 16 16"><rect x="1" y="3" width="12" height="12" fill="none" stroke="#a27bab"/><path d="M4 8 l3 3 l8 -9" fill="none" stroke="#a27bab" stroke-width="2"/></svg>Beveled Mirrors? No problem!</div>
  <div><svg width="16" height="16" viewBox="0 0 16 16"><rect x="1" y="3" width="12" height="12" fill="none" stroke="#a27bab"/><path d="M4 8 l3 3 l8 -9" fill="none" stroke="#a27bab" stroke-width="2"/></svg>DIY Install within minutes</div>
  <div><svg width="16" height="16" viewBox="0 0 16 16"><rect x="1" y="3" width="12" height="12" fill="none" stroke="#a27bab"/><path d="M4 8 l3 3 l8 -9" fill="none" stroke="#a27bab" stroke-width="2"/></svg>Install with mirror still on wall</div>
  <div><svg width="16" height="16" viewBox="0 0 16 16"><rect x="1" y="3" width="12" height="12" fill="none" stroke="#a27bab"/><path d="M4 8 l3 3 l8 -9" fill="none" stroke="#a27bab" stroke-width="2"/></svg>Guaranteed to fit any mirror, any size</div>
  <div><svg width="16" height="16" viewBox="0 0 16 16"><rect x="1" y="3" width="12" height="12" fill="none" stroke="#a27bab"/><path d="M4 8 l3 3 l8 -9" fill="none" stroke="#a27bab" stroke-width="2"/></svg>100% Satisfaction Guarantee</div>
  <div><svg width="16" height="16" viewBox="0 0 16 16"><rect x="1" y="3" width="12" height="12" fill="none" stroke="#a27bab"/><path d="M4 8 l3 3 l8 -9" fill="none" stroke="#a27bab" stroke-width="2"/></svg>Style selections to match any home decor</div>
  <div><svg width="16" height="16" viewBox="0 0 16 16"><rect x="1" y="3" width="12" height="12" fill="none" stroke="#a27bab"/><path d="M4 8 l3 3 l8 -9" fill="none" stroke="#a27bab" stroke-width="2"/></svg>Extends beyond mirror to hide ugly edges</div>
  <div><svg width="16" height="16" viewBox="0 0 16 16"><rect x="1" y="3" width="12" height="12" fill="none" stroke="#a27bab"/><path d="M4 8 l3 3 l8 -9" fill="none" stroke="#a27bab" stroke-width="2"/></svg>Outstanding customer support</div>
</div>

<div class="abs intro-buttons">
  <a class="btn btn-outline">SHOP NOW FREE SAMPLE</a>
  <a class="btn btn-outline">BEFORE &amp; AFTER GALLERY</a>
</div>

<section class="abs how">
  <h2 class="section-title">HOW IT WORKS</h2>
  <div class="abs step-card" style="left:113px">
    <div class="badge">STEP<b>1</b></div>
    <div class="pic" role="img" aria-label="Yellow tape measure" style="background:radial-gradient(circle at 40% 55%,#f2cc2e 0%,#e0b21f 35%,#fff 62%)"></div>
    <div class="cap">MEASURE YOUR MIRROR</div>
  </div>
  <div class="abs step-card" style="left:447px">
    <div class="badge">STEP<b>2</b></div>
    <div class="pic" role="img" aria-label="Stacked corner samples of frame mouldings" style="background:radial-gradient(ellipse at 50% 55%,#3a2a20 0%,#6b4b34 30%,#b09a82 45%,#fff 62%)"></div>
    <div class="cap">CHOOSE A FRAME</div>
  </div>
  <div class="abs step-card" style="left:781px">
    <div class="badge">STEP<b>3</b></div>
    <div class="pic" role="img" aria-label="Woman fitting a frame onto a bathroom mirror" style="background:linear-gradient(135deg,#cfd6dc,#e9e6e0 50%,#3d3a48)"></div>
    <div class="cap">EASY NO TOOLS INSTALLATION</div>
  </div>
  <svg class="abs" style="left:418px;top:288px" width="30" height="10"><path d="M0 5h26M20 1l6 4-6 4" stroke="#aaa" fill="none" stroke-dasharray="3 2"/></svg>
  <svg class="abs" style="left:752px;top:288px" width="30" height="10"><path d="M0 5h26M20 1l6 4-6 4" stroke="#aaa" fill="none" stroke-dasharray="3 2"/></svg>
</section>

<h2 class="abs section-title featured-title">FEATURED PRODUCT</h2>

<div class="abs tile" style="left:113px;top:2304px"><div class="pic" role="img" aria-label="Mirror with silver contemporary frame" style="background:linear-gradient(135deg,#8c8c88,#d9dad8 40%,#f0f0ee)"></div><div class="strip">CONTEMPORARY SILVER<span class="stars">★★★★★</span></div></div>
<div class="abs tile hover" style="left:444px;top:2304px"><div class="pic" role="img" aria-label="Mirror with bronze frame" style="background:linear-gradient(135deg,#6a4a2e,#c8b59c 40%,#ece7e0)"></div><div class="strip">COASTAL BRONZE<span class="stars">★★★★★</span></div><span class="shop">SHOP NOW</span></div>
<div class="abs tile" style="left:774px;top:2304px"><div class="pic" role="img" aria-label="Mirror with black and silver frame" style="background:linear-gradient(135deg,#2a2a2a,#9a9a98 40%,#e8e8e6)"></div><div class="strip">COASTAL BLACK SILVER<span class="stars">★★★★★</span></div></div>
<div class="abs tile" style="left:113px;top:2549px"><div class="pic" role="img" aria-label="Mirror with espresso brown frame" style="background:linear-gradient(135deg,#3a2618,#a38c76 40%,#eeeae5)"></div><div class="strip">HAMPTON ESPRESSO<span class="stars">★★★★★</span></div></div>
<div class="abs tile" style="left:444px;top:2549px"><div class="pic" role="img" aria-label="Mirror with dark java frame" style="background:linear-gradient(135deg,#2b1d16,#8e7866 40%,#ebe6e0)"></div><div class="strip">HAMPTON JAVA<span class="stars">★★★★★</span></div></div>
<div class="abs tile" style="left:774px;top:2549px"><div class="pic" role="img" aria-label="Mirror with simple silver frame" style="background:linear-gradient(135deg,#9a9a9a,#dcdcdc 40%,#f3f3f3)"></div><div class="strip">SIMPLY SILVER<span class="stars">★★★★★</span></div></div>
<span class="abs arrow-side" style="left:50px">&lsaquo;</span>
<span class="abs arrow-side" style="left:1125px">&rsaquo;</span>
<a class="abs btn btn-outline featured-btn">SHOP ALL FRAMES</a>

<section class="abs ba">
  <h2 class="section-title">CUSTOMER BEFORE/AFTER MIRROR FRAME KIT PHOTOS</h2>
  <svg class="abs ba-corner" style="left:96px;top:106px" viewBox="0 0 40 40"><path d="M0 40 V0 H40" fill="none" stroke="#c7a7cf" stroke-width="6"/></svg>
  <div class="abs ba-collage" role="img" aria-label="Customer bathroom mirrors before and after framing">
    <div></div><div></div><div></div><div></div>
  </div>
  <svg class="abs ba-corner" style="left:556px;top:436px" viewBox="0 0 40 40"><path d="M40 0 V40 H0" fill="none" stroke="#c7a7cf" stroke-width="6"/></svg>
  <p class="abs ba-text">Glassvela's Do-It-Yourself, before and after photo gallery, features mirror frames from some of our past clients. Do you want to be featured on our site as well? Email us before and after photos of your bathroom and your new frame, along with a quick note about how our DIY mirror frames helped improve your home and we will post YOUR success too!</p>
  <a class="abs ba-btn">BEFORE &amp; AFTER GALLERY</a>
</section>

<section class="abs guarantee">
  <div class="pic" role="img" aria-label="White bathroom vanity with a framed mirror" style="left:0;width:238px;background:linear-gradient(180deg,#d9d2c8 0%,#f1ece4 55%,#e6e2dc 100%)"></div>
  <div class="pic" role="img" aria-label="Bathroom vanity with a black framed mirror" style="left:246px;width:259px;background:linear-gradient(180deg,#cbbfae 0%,#3a3634 20%,#e8e2d8 40%,#3a3634 70%,#d9d3ca 100%)"></div>
  <div class="abs ribbon-tail" style="left:636px;border-left:22px solid transparent;border-right:0"></div>
  <div class="abs ribbon-tail" style="left:1078px;border-right:22px solid transparent;border-left:0"></div>
  <div class="abs ribbon">100% SATISFACTION GUARANTEE!</div>
  <p class="abs copy">Unsure? – Don't Worry, We Will Walk You<br>Through Every Step Of The Process.</p>
  <a class="abs btn btn-dark">Shop Now</a>
</section>

<section class="abs testi">
  <h2 class="section-title">WHAT OUR CUSTOMERS ARE SAYING</h2>
  <span class="arr" style="left:50px">&lsaquo;</span>
  <p class="quote">Great product and great service! Adding frames to our mirrors made all the difference in how the master bath looks. You can't beat Glassvela for the money!</p>
  <p class="who">Dana R., Seacliff Ca</p>
  <p class="stars">★★★★★</p>
  <span class="arr" style="left:1130px">&rsaquo;</span>
</section>

<footer class="abs footer">
  <div class="abs brand"><span class="mark"></span><span class="name">Glassvela</span></div>
  <div class="abs contact">
    88 Harbor Row, Suite 4, Seacliff,<br>CA 90000<br>(555) 014-2290<br>support@glassvela.com
  </div>
  <div class="abs col" style="left:418px">
    <h4>COMPANY INFO</h4>
    <ul><li>Glassvela.com</li><li>About Us</li><li>Privacy Policy</li><li>Terms &amp; Condition</li><li>Security on Our Site</li></ul>
  </div>
  <div class="abs col" style="left:633px">
    <h4>POLICIES &amp; PRODUCT INFO</h4>
    <ul><li>Our Guarantee</li><li>Shipping</li><li>Product Care</li><li>Return Policy</li></ul>
  </div>
  <div class="abs col" style="left:928px">
    <h4>SERVICES &amp; SUPPORT</h4>
    <ul><li>FAQ</li><li>Customer Support</li><li>Contact Us</li></ul>
  </div>
  <div class="abs badge-shape" style="left:926px"></div>
  <div class="abs badge-shape" style="left:1020px"></div>
  <p class="abs copy">© Copyright 2019 | Glassvela.com | All Rights Reserved</p>
</footer>

</body>
</html>
```